TOASTED COCONUT CHIPS

My company is a food company specialised in coconut products. The subject project is to design the package bag and respective simple shipping case for toasted coconut chips for two flavors: one is original and the other is cinnamon. I also need a logo design for the brand "pelvo".

I would like the bag looks simple, classy and attractive. Or the other way that it could look cute and fun.

The design will include two flavors: original/sea salt and cinnamon
The design need to be fit in 40g pouch bag and 20g bag.
Need the design of the bag and subsequently the shipping case.
Updates

Project Deadline Extended Reason: As per request of some designers, the deadline will be extended by 5 days. Added Tuesday, November 8, 2016

Target Market(s)

age 8 to 40
sell in cafeteria and vending machine

Industry/Entity Type

It Company

Logo Text

simple and direct

Requirements
Must have
• golden coconut chips picture on the front side.
• the bag should looks clean but attractive.
• Otherwise, it has to be very colourful to attract eye balls.
• I need the design can be fit in a 40g pouch and 20g cutie size bag
Should not have
• Should not look Asian food.

```html
<!DOCTYPE html>
<html lang="en">
<head>
<meta charset="utf-8">
<title>Pelvo Toasted Coconut Chips – Original 20 g</title>
<link rel="stylesheet" href="https://fonts.googleapis.com/css2?family=Satisfy&family=Oswald:wght@400;500&family=Lato:wght@400;700&display=swap">
<style>
  :root {
    --backdrop: #eeeeee;
    --bag: #ffffff;
    --crimp: #e3e3e3;
    --ink: #3a3a3a;
    --ink-soft: #4a4a4a;
    --brand: #3b2a22;
    --flavour: #1ea69c;
    --palm-mint: rgba(196, 226, 214, 0.75);
    --palm-fade: rgba(196, 226, 214, 0);
    --coconut-tone: rgba(120, 84, 60, 0.55);
    --coconut-flesh: rgba(228, 232, 236, 0.9);
    --chip-gold: rgba(227, 176, 106, 0.75);
    --chip-light: rgba(243, 215, 166, 0.9);
    --chip-fade: rgba(227, 176, 106, 0);
  }
  * { margin: 0; padding: 0; box-sizing: border-box; }
  html, body { width: 933px; height: 1200px; overflow: hidden; background: var(--backdrop); }
  .canvas { position: relative; width: 933px; height: 1200px; }

  .pouch {
    position: absolute; left: 75px; top: 58px; width: 783px; height: 1110px;
    background: var(--bag);
    overflow: hidden;
  }
  .crimp { position: absolute; left: 0; width: 100%; height: 50px; }
  .crimp--top { top: 0; }
  .crimp--bottom { bottom: 0; }

  .palm-art {
    position: absolute; left: -60px; top: 10px; width: 640px; height: 1060px;
    background: radial-gradient(closest-side at 50% 45%, var(--palm-mint) 0%, rgba(196,226,214,0.35) 55%, var(--palm-fade) 100%);
  }

  .brand {
    position: absolute; left: 455px; top: 165px;
    display: flex; align-items: center; gap: 12px;
  }
  .brand__dot { width: 20px; height: 20px; border-radius: 50%; background: var(--brand); }
  .brand__name {
    font-family: 'Lato', sans-serif; font-weight: 700; font-size: 44px;
    color: var(--brand); letter-spacing: 1px;
  }

  .product-title {
    position: absolute; left: 128px; top: 290px;
    font-family: 'Oswald', sans-serif; font-weight: 400;
    font-size: 82px; line-height: 90px; color: var(--ink);
  }
  .product-title span { display: block; }

  .claims {
    position: absolute; left: 98px; top: 483px;
    display: flex; align-items: stretch;
    font-family: 'Oswald', sans-serif; font-weight: 400;
    font-size: 15px; line-height: 19px; color: var(--ink-soft);
    text-transform: uppercase;
  }
  .claims__free-of { text-align: right; width: 268px; }
  .claims__free-label {
    writing-mode: vertical-rl; transform: rotate(180deg);
    font-weight: 500; font-size: 19px; letter-spacing: 1px;
    margin: 0 6px 0 5px; text-align: center; color: var(--ink);
  }
  .claims__divider { width: 1.5px; background: var(--ink-soft); margin-right: 8px; }

  .flavour {
    position: absolute; left: 428px; top: 572px;
    font-family: 'Satisfy', cursive; font-size: 64px; line-height: 80px; color: var(--flavour);
  }

  .coconut-art {
    position: absolute; left: 60px; top: 615px; width: 330px; height: 330px;
    background: radial-gradient(closest-side, var(--coconut-flesh) 0%, var(--coconut-tone) 55%, rgba(120,84,60,0) 100%);
  }
  .chips-art {
    position: absolute; left: 215px; top: 670px; width: 540px; height: 370px;
    background: radial-gradient(closest-side, var(--chip-light) 0%, var(--chip-gold) 55%, var(--chip-fade) 100%);
  }

  .net-weight {
    position: absolute; left: 87px; top: 926px;
    font-family: 'Lato', sans-serif; font-weight: 400; font-size: 21px; color: var(--ink);
  }
</style>
</head>
<body>
<main class="canvas">
  <section class="pouch">
    <svg class="crimp crimp--top" viewBox="0 0 783 50" preserveAspectRatio="none" aria-hidden="true">
      <g stroke="var(--crimp)" stroke-width="2">
        <line x1="0" y1="8" x2="783" y2="8"/><line x1="0" y1="17" x2="783" y2="17"/>
        <line x1="0" y1="26" x2="783" y2="26"/><line x1="0" y1="35" x2="783" y2="35"/>
        <line x1="0" y1="44" x2="783" y2="44"/>
      </g>
    </svg>

    <div class="palm-art" role="img" aria-label="Faint mint palm tree illustration in the background"></div>

    <div class="brand">
      <span class="brand__dot"></span>
      <span class="brand__name">Pelvo</span>
    </div>

    <h1 class="product-title"><span>TOASTED</span><span>COCONUT CHIPS</span></h1>

    <div class="claims">
      <p class="claims__free-of">Gluten, Dairy , Cholesterol,<br>Preservatives, Artifical Colors,<br>Artifical Flavours</p>
      <span class="claims__free-label">FREE</span>
      <span class="claims__divider"></span>
      <p class="claims__benefits">All natural ingredients<br>Not fired, vegan<br>Good source of fiber</p>
    </div>

    <p class="flavour">Original</p>

    <div class="chips-art" role="img" aria-label="Pile of golden toasted coconut chips"></div>
    <div class="coconut-art" role="img" aria-label="Illustration of a cracked half coconut with white flesh"></div>

    <p class="net-weight">Net Wt: 20 g (0.7 oz)</p>

    <svg class="crimp crimp--bottom" viewBox="0 0 783 50" preserveAspectRatio="none" aria-hidden="true">
      <g stroke="var(--crimp)" stroke-width="2">
        <line x1="0" y1="6" x2="783" y2="6"/><line x1="0" y1="15" x2="783" y2="15"/>
        <line x1="0" y1="24" x2="783" y2="24"/><line x1="0" y1="33" x2="783" y2="33"/>
        <line x1="0" y1="42" x2="783" y2="42"/>
      </g>
    </svg>
  </section>
</main>
</body>
</html>
```